Satchel & Compass needs new business card design

I need a new business card design. I'm looking for out-of-the-box design which represents the freedom of being a location independent entrepreneur.
I offer coaching, retreats and trips.
I would like to see designs with and without the photo.
Colors I use are black (#000000), green (#25A796) and brown (#D7C38C)
Website satchelandcompass.com

Target Market(s)

location independent entrepreneurs, digital nomads, people looking to swap the 9 to 5 for a lifestyle business

Industry/Entity Type

Business

Contact Information for Business Card

Petra Varga
Your Lifestyle Business Coach, Retreat & Trip Leader
http://satchelandcompass.com
hello@satchelandcompass.com
Live a life you don't need a holiday from

Font styles to use
Serif
Sans Serif

Requirements
Must have
• One side should contain only the logo. I would also consider having the "Live a life you don't need a holiday from" on that side too (depending on how it looks)
• Please show both sides on the designs.

```html
<!DOCTYPE html>
<html lang="en">
<head>
<meta charset="utf-8">
<title>Satchel &amp; Compass — Business Card</title>
<link rel="stylesheet" href="https://fonts.googleapis.com/css2?family=Source+Sans+3:wght@400;600;700&display=swap">
<style>
  :root {
    --ink: #1f1d1e;
    --black: #000000;
    --brown: #d7c38c;
    --green: #25a796;
    --paper: #ececec;
    --stage: #e7e3de;
    --white: #ffffff;
  }
  html, body {
    margin: 0;
    padding: 0;
    width: 1200px;
    height: 900px;
    overflow: hidden;
    background: var(--stage);
    font-family: "Source Sans 3", "Myriad Pro", Arial, sans-serif;
  }
  .canvas {
    position: relative;
    width: 1200px;
    height: 900px;
  }
  .card {
    position: absolute;
    width: 555px;
    height: 345px;
    overflow: hidden;
    box-shadow: 0 6px 18px rgba(0, 0, 0, 0.12);
  }
  .card--front {
    left: 238px;
    top: 60px;
    background: var(--brown);
    border-radius: 0 56px 0 32px;
  }
  .card--back {
    left: 460px;
    top: 518px;
    width: 558px;
    background: var(--paper);
    border-radius: 56px 0 32px 0;
  }
  .holder {
    position: absolute;
    left: 32px;
    top: 28px;
    color: var(--ink);
  }
  .holder__name {
    margin: 0 0 4px;
    font-size: 18px;
    font-weight: 700;
  }
  .holder__role {
    margin: 0;
    font-size: 15px;
    line-height: 20px;
    font-weight: 400;
  }
  .brand-name {
    position: absolute;
    margin: 0;
    color: var(--ink);
    font-weight: 600;
    white-space: nowrap;
    letter-spacing: 0.5px;
  }
  .card--front .brand-name {
    right: 40px;
    top: 132px;
    font-size: 32px;
  }
  .card--back .brand-name {
    left: 0;
    right: 0;
    top: 140px;
    text-align: center;
    font-size: 44px;
  }
  .contact {
    position: absolute;
    left: 32px;
    top: 211px;
    margin: 0;
    padding: 0;
    list-style: none;
    color: var(--ink);
    font-size: 15px;
    line-height: 19px;
  }
  .contact__item {
    display: flex;
    align-items: center;
    gap: 9px;
  }
  .contact__icon {
    width: 10px;
    height: 10px;
    flex: none;
  }
  .tagline-band {
    position: absolute;
    left: 0;
    bottom: 0;
    width: 555px;
    height: 66px;
    background: var(--ink);
    clip-path: polygon(0 0, 477px 0, 555px 66px, 0 66px);
  }
  .tagline-band__text {
    position: absolute;
    left: 56px;
    top: 21px;
    margin: 0;
    color: var(--white);
    font-size: 16.5px;
    font-weight: 400;
    letter-spacing: 0.2px;
    text-transform: uppercase;
  }
</style>
</head>
<body>
<main class="canvas">

  <section class="card card--front" aria-label="Business card front">
    <div class="holder">
      <p class="holder__name">Petra Varga</p>
      <p class="holder__role">Your Lifestyle Business</p>
      <p class="holder__role">Coach Retreat &amp; Trip Leader</p>
    </div>

    <p class="brand-name">Satchel &amp; Compass</p>

    <ul class="contact">
      <li class="contact__item">
        <svg class="contact__icon" viewBox="0 0 10 10" aria-hidden="true">
          <rect x="0.5" y="1.5" width="9" height="7" fill="#1f1d1e"/>
          <path d="M0.8 2 L5 5.4 L9.2 2" fill="none" stroke="#d7c38c" stroke-width="1"/>
        </svg>
        <span>hello@satchelandcompass.com</span>
      </li>
      <li class="contact__item">
        <svg class="contact__icon" viewBox="0 0 10 10" aria-hidden="true">
          <circle cx="5" cy="5" r="4.6" fill="#1f1d1e"/>
          <path d="M2.5 3.2 L4.6 2.6 L5.4 4.4 L4 5.6 L4.6 7.6 L3 7 Z M6.2 5.8 L7.8 5.2 L7.2 7.4 Z" fill="#d7c38c"/>
        </svg>
        <span>www.satchelandcompass.com</span>
      </li>
    </ul>

    <div class="tagline-band">
      <p class="tagline-band__text">Live a life you don't need a holiday from</p>
    </div>
  </section>

  <section class="card card--back" aria-label="Business card back">
    <p class="brand-name">Satchel &amp; Compass</p>
  </section>

</main>
</body>
</html>
```